Briefkopf und Visitenkarte für Kanzlei
Zielgruppe
Wir sind eine Kanzlei mit Sitz in Neuss und den Schwerpunkten im Arbeitsrecht und Strafrecht. Unser Rechtsanwalt Kerem Yalçıntaş ist zugleich Fachanwalt für das Arbeitsrecht. Unsere Zielgruppe sind alle Menschen, die in diesen beiden Gebieten Rechtsberatung oder Vertretung suchen. Nähere Informationen über uns findet Ihr auf www.hovbera-kanzlei.de
Aufgabenstellung
Was ich möchte:
- das Design sollte schlicht sein und nicht zu dick auftragen. Zu schlicht ist aber auch nicht gut, schlielich soll erkennbar sein, dass die Briefvorlage nicht von einem Laien ertellt wurde, sondern von einem Designer.
- Farbakzente wie marineblau und gold sind gewünscht, allerdings nicht zu übertrieben, weil das sonst vom Textinhalt ablenkt und zu viel Tinte verbraucht.
- Der Briefkopf sollte folgende Informationen anzeigen: Fachanwaltstitel, Anschrift, Kontaktmöglichkeiten wie Telefon, Fax, E-Mail und Webseite, Öffnungszeiten, Bankverbindung und Umsatzsteuer IDNr.
- Eine Kopfzeile oder Fußzeile mit dem Kanzleinamen - / Logo, die auch ab Seite 1. weitergeführt wird.
- Die Seitenzahl sollte ersichtlich sein.
- Die Endddatei sollte hinsichtlich der angegebenen Daten (wie bspw. Telefonnummer und Anschrift) leicht veränderbar sein (gewünscht sind word und rtf als Dateiformat)
- Die Schriftart für den Schriftzug Halls Of Falcons ist Trajan pro.
Was ich nicht möchte:
- Keine Wasserzeichen in der Mitte des Textes. Das lenkt von der Schrift ab.
- Die Enddatei sollte nicht groß sein (idealerweise unter 0,75 -1 mb), da wir unsere Schreiben oft per Mail versenden und der Anhang dadurch zu groß würde.

```html
<!DOCTYPE html>
<html lang="de">
<head>
<meta charset="utf-8">
<title>Kanzlei Kerem Yalçıntaş – Geschäftsausstattung</title>
<link href="https://fonts.googleapis.com/css2?family=Cinzel:wght@400;500&family=Arimo:wght@400;700&display=swap" rel="stylesheet">
<style>
:root{
  --board:#b3b3b3;
  --paper:#ffffff;
  --navy:#24347e;
  --gold:#c8a95a;
  --taupe:#8a7d6a;
  --ink:#1d1d1d;
  --rule:#d8c9a0;
}
*{margin:0;padding:0;box-sizing:border-box}
html,body{width:1200px;height:1200px;overflow:hidden;background:var(--board)}
body{position:relative;font-family:"Arimo",Arial,sans-serif;color:var(--ink)}
.piece{position:absolute;background:var(--paper);box-shadow:5px 6px 8px rgba(0,0,0,.35)}
.abs{position:absolute}
.seal{position:absolute;border-radius:50%;background:var(--gold)}
.person-name{font-family:"Cinzel",serif;color:var(--navy);white-space:nowrap;line-height:1}
.coop-name{font-family:"Arimo",Arial,sans-serif;font-weight:400;color:var(--navy);white-space:nowrap;line-height:1;text-align:center}
.title{color:var(--taupe);white-space:nowrap;letter-spacing:.02em;line-height:1}
.band{position:absolute;left:0;bottom:0;width:100%}
.web{position:absolute;color:#3a3320;white-space:nowrap;display:flex;align-items:center;gap:4px;line-height:1}
.label{color:var(--navy)}

/* letterhead */
.letter{left:48px;top:56px;width:504px;height:712px}
.letter .sender{left:80px;top:117px;font-size:6px;color:#666;white-space:nowrap}
.letter .divider{left:356px;top:33px;width:1px;height:645px;background:var(--rule)}
.letter .info{left:366px;top:31px;font-size:6.2px;line-height:9.6px;width:134px}
.letter .info p{margin-bottom:8px}
.letter .fold{left:10px;height:1px;width:14px;background:#ddd}
.letter .page-no{left:43px;top:664px;font-family:"Times New Roman",serif;font-size:11px}
.member{text-align:center;font-size:7px;line-height:10px}

/* envelopes */
.env-back{left:593px;top:51px;width:557px;height:279px}
.env-front{left:593px;top:480px;width:557px;height:280px}
.env-flap{position:absolute;left:593px;top:401px;width:557px;height:80px}

/* cards */
.card-front{left:65px;top:863px;width:409px;height:266px}
.card-back{left:660px;top:862px;width:407px;height:263px}
.card-front .contact{left:197px;top:131px;font-size:11.5px;line-height:17px;color:#333;white-space:nowrap}
.card-front .contact .tab{display:inline-block;width:38px}
</style>
</head>
<body>

<svg width="0" height="0" style="position:absolute">
  <defs>
    <linearGradient id="goldBand" x1="0" x2="1">
      <stop offset="0" stop-color="#a8863a"/>
      <stop offset=".45" stop-color="#efe2a8"/>
      <stop offset=".75" stop-color="#c8a95a"/>
      <stop offset="1" stop-color="#e9d894"/>
    </linearGradient>
  </defs>
</svg>

<!-- Letterhead -->
<section class="piece letter">
  <div class="seal" style="left:52px;top:20px;width:48px;height:48px" aria-hidden="true"></div>
  <div class="abs person-name" style="left:110px;top:30px;font-size:17px">Kerem Yalçıntaş</div>
  <div class="abs title" style="left:111px;top:50px;font-size:8.5px">FACHANWALT FÜR ARBEITSRECHT</div>
  <div class="abs sender">RA Kerem Yalçıntaş • Ahornstraße 22 • 52317 Hovbergen</div>

  <div class="abs fold" style="top:239px"></div>
  <div class="abs fold" style="top:356px;left:15px;width:22px"></div>
  <div class="abs fold" style="top:477px"></div>

  <div class="abs divider"></div>
  <div class="abs info">
    <p style="margin-left:3px">Ahornstraße 22 - 52317 Hovbergen<br>
      <span class="label">Kontakt:</span><br>
      <span class="label">Tel:</span>&nbsp;&nbsp;&nbsp;&nbsp;&nbsp; +49 (0) 2410 / 48 20 117<br>
      <span class="label">Fax:</span>&nbsp;&nbsp;&nbsp;&nbsp; +49 (0) 2410 / 48 20 118<br>
      <span class="label">E-Mail:</span> kyalcintas@hovbera-kanzlei.de</p>
    <p><span class="label">Öffnungszeiten:</span><br>
      Montag bis Freitag<br>8:30 Uhr bis 13:00 Uhr<br>und 14:00 Uhr bis 17.00 Uhr</p>
    <p><span class="label">Bankverbindung:</span><br>
      Kerem Yalçıntaş<br>IBAN: DEXX XXXX XXXX XXXX XXXX X<br>BIC: XXXXXXXX<br>Rheinbank Nord</p>
  </div>

  <div class="abs member" style="left:367px;top:606px;width:120px">Grunder und Mitglied der<br>Anwaltskooperation:</div>
  <div class="seal" style="left:416px;top:636px;width:22px;height:22px" aria-hidden="true"></div>
  <div class="abs coop-name" style="left:367px;top:664px;width:120px;font-size:9.5px">Halls Of Falcons</div>
  <div class="abs page-no">-1-</div>

  <svg class="band" width="504" height="20" viewBox="0 0 504 20" aria-hidden="true">
    <polygon points="0,10 351,10 343,20 0,20" fill="var(--navy)"/>
    <polygon points="362,0 504,0 504,20 343,20" fill="url(#goldBand)"/>
  </svg>
  <div class="web" style="left:381px;top:696px;font-size:6.5px">
    <svg width="8" height="8" viewBox="0 0 10 10" aria-hidden="true"><g fill="none" stroke="#3a3320" stroke-width=".8"><circle cx="5" cy="5" r="4.3"/><ellipse cx="5" cy="5" rx="2" ry="4.3"/><path d="M.7 5h8.6M1.5 2.8h7M1.5 7.2h7"/></g></svg>
    www.hovbera-kanzlei.de
  </div>
</section>

<!-- Envelope back -->
<section class="piece env-back">
  <svg class="abs" style="left:0;top:0" width="557" height="82" viewBox="0 0 557 82" aria-hidden="true">
    <path d="M3 0 L24 70 Q28 78 38 78 L520 78 Q530 78 533 70 L556 0" fill="#fff" stroke="#ddd" stroke-width="1"/>
    <path d="M38 80 L520 80" stroke="#ececec" stroke-width="3"/>
  </svg>
  <div class="seal" style="left:251px;top:13px;width:54px;height:54px" aria-hidden="true"></div>
</section>

<!-- Envelope front with flap -->
<svg class="env-flap" viewBox="0 0 557 80" aria-hidden="true">
  <path d="M1 79 L25 8 Q28 0 38 0 L519 0 Q529 0 532 8 L556 79 Z" fill="#fff"/>
  <line x1="1" y1="79.5" x2="556" y2="79.5" stroke="#777" stroke-width="1"/>
</svg>
<div class="seal" style="left:845px;top:413px;width:54px;height:54px" aria-hidden="true"></div>
<section class="piece env-front">
  <div class="seal" style="left:32px;top:30px;width:48px;height:48px" aria-hidden="true"></div>
  <div class="abs person-name" style="left:90px;top:40px;font-size:16px">Kerem Yalçıntaş</div>
  <div class="abs title" style="left:91px;top:59px;font-size:8.5px;color:#222">FACHANWALT FÜR ARBEITSRECHT</div>
  <div class="abs member" style="left:80px;top:171px;width:120px">Grunder und Mitglied der<br>Anwaltskooperation:</div>
  <div class="seal" style="left:128px;top:200px;width:24px;height:24px" aria-hidden="true"></div>
  <div class="abs coop-name" style="left:70px;top:229px;width:140px;font-size:10px">Halls Of Falcons</div>
  <div class="abs" style="left:63px;top:250px;font-size:12px;color:#333;white-space:nowrap">Ahornstraße 22 - 52317 Hovbergen</div>
  <svg class="band" width="557" height="20" viewBox="0 0 557 20" aria-hidden="true">
    <polygon points="0,8 407,8 395,20 0,20" fill="var(--navy)"/>
    <polygon points="416,0 557,0 557,20 395,20" fill="url(#goldBand)"/>
  </svg>
  <div class="web" style="left:440px;top:263px;font-size:8.5px">
    <svg width="10" height="10" viewBox="0 0 10 10" aria-hidden="true"><g fill="none" stroke="#3a3320" stroke-width=".8"><circle cx="5" cy="5" r="4.3"/><ellipse cx="5" cy="5" rx="2" ry="4.3"/><path d="M.7 5h8.6M1.5 2.8h7M1.5 7.2h7"/></g></svg>
    www.hovbera-kanzlei.de
  </div>
</section>

<!-- Business card front -->
<section class="piece card-front">
  <div class="seal" style="left:62px;top:21px;width:64px;height:64px" aria-hidden="true"></div>
  <div class="abs person-name" style="left:142px;top:35px;font-size:20px">Kerem Yalçıntaş</div>
  <div class="abs title" style="left:143px;top:60px;font-size:11px">FACHANWALT FÜR ARBEITSRECHT</div>

  <div class="abs member" style="left:14px;top:131px;width:150px;font-size:10px;line-height:14px">Grunder und Mitglied der<br>Anwaltskooperation:</div>
  <div class="seal" style="left:72px;top:166px;width:36px;height:36px" aria-hidden="true"></div>
  <div class="abs coop-name" style="left:4px;top:207px;width:170px;font-size:13px">Halls Of Falcons</div>

  <div class="abs" style="left:175px;top:133px;width:1px;height:95px;background:var(--rule)"></div>
  <div class="abs contact">
    Ahornstraße 22 - 52317 Hovbergen<br>
    <span class="label" style="display:inline-block;margin-top:13px">Kontakt:</span><br>
    <span class="label tab">Tel:</span>+49 (0) 2410 / 48 20 117<br>
    <span class="label tab">Fax:</span>+49 (0) 2410 / 48 20 118<br>
    <span class="label">E-Mail:</span> kyalcintas@hovbera-kanzlei.de
  </div>

  <svg class="band" width="409" height="24" viewBox="0 0 409 24" aria-hidden="true">
    <line x1="0" y1="0.5" x2="244" y2="0.5" stroke="var(--gold)" stroke-width="1"/>
    <polygon points="0,14 234,14 224,24 0,24" fill="var(--navy)"/>
    <polygon points="246,0 409,0 409,24 224,24" fill="url(#goldBand)"/>
  </svg>
  <div class="web" style="left:261px;top:248px;font-size:11.5px">
    <svg width="13" height="13" viewBox="0 0 10 10" aria-hidden="true"><g fill="none" stroke="#3a3320" stroke-width=".7"><circle cx="5" cy="5" r="4.3"/><ellipse cx="5" cy="5" rx="2" ry="4.3"/><path d="M.7 5h8.6M1.5 2.8h7M1.5 7.2h7"/></g></svg>
    www.hovbera-kanzlei.de
  </div>
</section>

<!-- Business card back -->
<section class="piece card-back">
  <div class="seal" style="left:172px;top:78px;width:64px;height:64px" aria-hidden="true"></div>
  <div class="abs coop-name" style="left:0;top:152px;width:407px;font-size:29px">Halls Of Falcons</div>
</section>

</body>
</html>
```